International freight forwarder experienced in perishable handling needs a web design

We need a website designed that will allow us to capture more customers through the website. We would like a visually appealing design that is not so heavy on text. Our business covers the logistics and freight forwarding industries and we have offices in South America and the USA. Our main customers are importers USA, Europe, Asia and Russia and we currently work almost exclusively with perishable products such as fresh cut flowers, fresh exotics fruits, cacao, fresh fish etc. We would like to convey a fresh, modern approach to freight forwarding focusing on concepts such as - time sensitive, anytime-anywhere delivery, innovation, experience, reliability and confidence. Should include links with Plumetta and Worvanet. Our core solutions include: Core Services
*Air Freight
*Ocean Freight
*Warehousing & Distribution
Our industry solutions cover
*Flowers
*FMCG including, fruits, vegetables
*Live animals
*Automotive
*Consumer Goods
*Industrial
*Oil & Gas
*Pharma
* Event logistics
* Project logistics

Target Market(s)

Importers in Europe, USA, Asia, Middle East and Russia

Number of Pages Required

4 page

Font styles to use
Sans Serif

Colors
a1cd39
606060
000000

Requirements
Must have
• Photos of fresh cut flowers, FMCG such as cacao, fresh fish (packaged for shipping), fresh exotic fruits, pharma products (packaged for shipping), oil and gas etc. Internal customer login access
Nice to have
• Photos of cargo shipping carriers and cargo airline carriers. Features similar to those of following website http://www.brolvacargo.com/eng/main/index.jsp?FromURL=web
Should not have
• Too much text, needs to be visually pleasing

```html
<!DOCTYPE html>
<html lang="en">
<head>
<meta charset="utf-8">
<title>Vantora Freight Group</title>
<link href="https://fonts.googleapis.com/css2?family=Lato:wght@400;700;900&family=Oswald:wght@600&display=swap" rel="stylesheet">
<style>
:root{
  --green:#8ab92c;
  --green-light:#a1cd39;
  --grey:#606060;
  --dark:#1f1f1f;
  --black:#000;
  --soft:#f7f7f7;
  --band:#e5e5e5;
  --line:#cfcfcf;
  --white:#fff;
}
*{margin:0;padding:0;box-sizing:border-box}
html,body{width:842px;height:1200px;overflow:hidden}
body{font-family:'Lato',sans-serif;color:var(--grey);background:var(--white);position:relative}
.abs{position:absolute}
/* header */
.header{top:0;left:0;width:842px;height:83px;background:var(--white);border-bottom:2px solid #555}
.brand{left:98px;top:40px;font-size:18px;font-weight:700;color:#333;letter-spacing:-.3px}
.brand-mark{display:inline-block;width:10px;height:10px;border-radius:50%;background:var(--green-light);margin-right:6px;vertical-align:1px}
.brand-sub{left:146px;top:67px;font-size:6px;letter-spacing:2px;color:#999}
.phone-top{right:98px;top:20px;font-size:12.5px;color:#333;display:flex;align-items:center;gap:4px}
.nav{top:59px;left:319px;display:flex;font-size:10px;font-weight:700;color:#333}
.nav a{color:inherit;text-decoration:none;margin-right:24px;position:relative;height:24px}
.nav a:last-child{margin-right:0}
.nav a.active{color:var(--green)}
.nav a.active::after{content:"";position:absolute;left:0;right:0;bottom:0;height:2px;background:var(--green-light)}
/* hero */
.hero{top:83px;left:0;width:842px;height:366px;background:linear-gradient(180deg,#7d8a93 0%,#5c6a6e 40%,#3b4552 70%,#1c2230 100%)}
.hero-arrow{top:252px;width:26px;height:26px;border-radius:50%;background:var(--white);display:flex;align-items:center;justify-content:center}
.hero-title{left:98px;top:362px;font-family:'Oswald',sans-serif;font-weight:600;font-size:28px;line-height:32px;color:var(--white);letter-spacing:-.3px}
/* about */
.about{top:449px;left:0;width:842px;height:242px;background:var(--soft)}
.about h2{font-weight:400;font-size:19px;color:#333}
.about h2 b{font-weight:700}
.about-title{left:96px;top:470px}
.about-title .brand-inline{font-weight:700;font-size:17px;color:#333}
.rule{height:0;border-top:1px dashed var(--line)}
.about-text{left:96px;top:506px;width:398px;font-size:9.4px;line-height:14px}
.solutions-title{left:96px;top:553px}
.list{top:588px;list-style:none;font-size:9.6px;line-height:16px}
.list li::before{content:"• "}
/* inquiry */
.inquiry{left:522px;top:406px;width:224px;height:284px;background:var(--white);border-radius:4px 4px 0 0;box-shadow:0 1px 4px rgba(0,0,0,.15)}
.inquiry h3{text-align:center;font-weight:400;font-size:23px;color:#333;margin-top:10px}
.dots{display:flex;justify-content:center;gap:3px}
.dots i{width:3px;height:3px;border-radius:50%;background:#aaa;display:block}
.field{position:absolute;left:15px;width:193px;height:21px;border:1px solid var(--line);border-radius:2px;font-size:8px;font-weight:700;color:#555;padding:5px 12px}
.field.msg{height:59px}
.submit{position:absolute;left:15px;top:230px;width:193px;height:30px;background:var(--green);color:var(--white);font-weight:700;font-size:11.5px;display:flex;align-items:center;justify-content:center;border-radius:2px}
/* services */
.services{top:691px;left:0;width:842px;height:267px;background:var(--band)}
.services-title{left:0;width:842px;top:713px;text-align:center;font-size:22px;color:#333}
.card{top:755px;width:204px;height:158px;background:var(--white);border-radius:8px;text-align:center}
.card .icon{width:64px;height:64px;border-radius:50%;margin:10px auto 0;background:radial-gradient(circle,#fff 20%,#d8d8d8 100%);display:flex;align-items:center;justify-content:center}
.card h4{font-weight:400;font-size:13px;color:#333;margin-top:7px}
.card p{font-size:8.4px;line-height:12px;padding:0 10px;margin-top:4px}
.num{position:absolute;left:84px;bottom:-16px;width:36px;height:36px;border-radius:50%;background:var(--white);display:flex;align-items:center;justify-content:center}
.num span{width:22px;height:22px;border-radius:50%;background:#2b2b2b;color:#fff;font-size:12px;font-weight:700;display:flex;align-items:center;justify-content:center}
/* newsletter */
.newsletter{top:958px;left:0;width:842px;height:45px;background:var(--green)}
.nl-title{left:147px;top:971px;font-size:16px;color:var(--white)}
.nl-sub{left:342px;top:975px;font-size:10.5px;color:#1d2a05}
.nl-input{left:500px;top:972px;width:182px;height:20px;background:var(--white);font-size:9px;color:#888;padding:4px 12px}
.nl-btn{left:682px;top:972px;width:63px;height:20px;background:#333;color:#fff;font-weight:700;font-size:10px;display:flex;align-items:center;justify-content:center}
/* footer */
.footer{top:1003px;left:0;width:842px;height:167px;background:var(--dark)}
.f-head{top:1025px;font-size:13px;color:var(--green-light)}
.f-rule{top:1046px;border-top:1px dashed #444;height:0}
.links{left:98px;top:1054px;list-style:none;font-size:9.4px;color:#eee;line-height:16.3px}
.links li::before{content:"→";font-size:7px;margin-right:7px;color:#aaa}
.news{left:219px;width:143px;font-size:8.4px;color:#bbb;line-height:11px}
.news b{display:block;font-style:italic;font-size:9px;color:#fff;margin-bottom:2px}
.contact{left:401px;top:1054px;font-size:8.5px;color:#eee;line-height:11.3px}
.c-row{display:flex;gap:8px;align-items:flex-start;margin-bottom:6px}
.c-row.big{font-size:10px;font-weight:700;margin-bottom:5px}
.map{left:578px;top:1059px;width:167px;height:87px;background:linear-gradient(135deg,#e8ecd9,#b8d3e8 55%,#d9dfc8);border:2px solid #fff}
.bottom{top:1170px;left:0;width:842px;height:30px;background:var(--black)}
.copy{left:96px;top:1180px;font-size:7.8px;color:#ccc}
.social{top:1177px;right:98px;display:flex;gap:6px}
.social span{width:18px;height:16px;background:#333;color:#eee;font-size:4.6px;display:flex;align-items:center;justify-content:center;border-radius:2px}
</style>
</head>
<body>

<header class="abs header">
  <div class="abs brand"><span class="brand-mark"></span>Vantora Freight</div>
  <div class="abs brand-sub">GROUP</div>
  <div class="abs phone-top">
    <svg width="11" height="11" viewBox="0 0 12 12"><circle cx="6" cy="6" r="5.3" fill="none" stroke="#8ab92c" stroke-width="1"/><path d="M4 3.5l1 1-.6.8c.4.8 1 1.4 1.8 1.8l.8-.6 1 1-.7.9C5.6 8.4 3.6 6.4 3.2 4.2z" fill="#8ab92c"/></svg>
    555 0142 7700
  </div>
  <nav class="abs nav">
    <a class="active">HOME</a><a>ABOUT US</a><a>OUR SERVICES</a><a>OUR NETWORK</a><a>NEWS</a><a>CONTACT US</a>
  </nav>
</header>

<section class="abs hero" role="img" aria-label="Container ship docked under port cranes at a cargo terminal"></section>
<div class="abs hero-arrow" style="left:38px"><svg width="8" height="10" viewBox="0 0 8 10"><path d="M6 1L2 5l4 4" fill="none" stroke="#555" stroke-width="1.2"/></svg></div>
<div class="abs hero-arrow" style="left:778px"><svg width="8" height="10" viewBox="0 0 8 10"><path d="M2 1l4 4-4 4" fill="none" stroke="#555" stroke-width="1.2"/></svg></div>
<h1 class="abs hero-title">Lorem ipsum dolor sit amet consectetuer<br>adipiscing elit sed</h1>

<section class="abs about"></section>
<h2 class="abs about-title" style="font-weight:400;font-size:19px;color:#333">About <span class="brand-inline">Vantora Freight</span> <span style="font-size:6px;letter-spacing:2px;color:#999">GROUP</span></h2>
<div class="abs rule" style="left:96px;top:498px;width:398px"></div>
<p class="abs about-text">Lorem ipsum dolor sit amet, consectetuer adipiscing elit, sed diam nonummy nibh euismod tincidunt ut laoreet dolore magna aliquam erat volutpat. Ut wisi enim ad minim veniam, quis nostrud exerci tation ullamcorper suscipit lobortis nisl ut aliquip ex ea commodo consequat.</p>
<h2 class="abs solutions-title" style="font-weight:400;font-size:19px;color:#333">Our <b>industry solutions</b> cover</h2>
<div class="abs rule" style="left:96px;top:583px;width:398px"></div>
<ul class="abs list" style="left:96px">
  <li>Flowers</li><li>FMCG including, fruits, vegetables</li><li>Live animals</li><li>Automotive</li><li>Consumer Goods</li>
</ul>
<ul class="abs list" style="left:299px">
  <li>Industrial</li><li>Oil &amp; Gas</li><li>Pharma</li><li>Event logistics</li><li>Project logistics</li>
</ul>

<form class="abs inquiry">
  <h3>Quick Inquiry</h3>
  <div class="rule" style="margin:6px 15px 0;border-top-style:solid"></div>
  <div class="dots" style="margin-top:-2px"><i></i><i></i><i></i></div>
  <div class="field" style="top:65px">Full Name</div>
  <div class="field" style="top:97px">Email Address</div>
  <div class="field" style="top:129px">Phone Number</div>
  <div class="field msg" style="top:160px">Message</div>
  <div class="submit">SUBMIT</div>
</form>

<section class="abs services"></section>
<h2 class="abs services-title" style="font-weight:400">Our Services</h2>
<div class="abs rule" style="left:324px;top:743px;width:194px;border-top:1px solid #999"></div>
<div class="abs dots" style="left:0;width:842px;top:742px"><i></i><i></i><i></i></div>

<article class="abs card" style="left:101px">
  <div class="icon"><svg width="40" height="20" viewBox="0 0 40 20"><path d="M2 12c8-1 20-4 34-6 2 0 2 2 0 3L18 14l-6 5h-3l3-5-7 1-2 2H1l1-3zM14 9l-4-6h3l8 5z" fill="#111"/></svg></div>
  <h4>Air Freight</h4>
  <p>Lorem ipsum dolor sit amet, consectetuer elit, sed diam nonummy nibh euismod tincidunt ut laoreet dolore magna aliquam erat volutpat.</p>
  <div class="num"><span>1</span></div>
</article>
<article class="abs card" style="left:318px">
  <div class="icon"><svg width="40" height="22" viewBox="0 0 40 22"><path d="M2 13h36l-5 7H7z M10 13V9h18v4 M14 9V5h8v4 M17 5V2h2v3" fill="#111" stroke="#111"/><path d="M12 10h2M16 10h2M20 10h2M24 10h2" stroke="#fff"/></svg></div>
  <h4>Ocean Freight</h4>
  <p>Lorem ipsum dolor sit amet, consectetuer elit, sed diam nonummy nibh euismod tincidunt ut laoreet dolore magna aliquam erat volutpat.</p>
  <div class="num"><span>2</span></div>
</article>
<article class="abs card" style="left:536px">
  <div class="icon"><svg width="34" height="24" viewBox="0 0 34 24"><path d="M1 9L17 2l16 7v3H1z M4 12h26v11H4z" fill="#111"/><path d="M9 15h16M9 18h16M9 21h16" stroke="#fff" stroke-width="1.2"/></svg></div>
  <h4>Warehousing &amp; Distribution</h4>
  <p>Lorem ipsum dolor sit amet, consectetuer elit, sed diam nonummy nibh euismod tincidunt ut laoreet dolore magna aliquam erat volutpat.</p>
  <div class="num"><span>3</span></div>
</article>

<section class="abs newsletter"></section>
<svg class="abs" style="left:98px;top:963px" width="34" height="34" viewBox="0 0 34 34"><rect x="2" y="8" width="26" height="22" rx="2" fill="#e8f2f8" stroke="#5a7d96"/><path d="M2 10l13 10 13-10" fill="none" stroke="#5a7d96"/><path d="M14 22l16-16 3 3-16 16-4 1z" fill="#3b3b3b"/></svg>
<div class="abs nl-title">Newsletter Signup</div>
<svg class="abs" style="left:300px;top:964px" width="30" height="32" viewBox="0 0 30 32"><path d="M2 2l12 14L2 30M12 2l12 14-12 14" fill="none" stroke="#fff" stroke-width="1.6"/></svg>
<div class="abs nl-sub">Signup For Free Email Updates</div>
<div class="abs nl-input">✉ Enter your email here</div>
<div class="abs nl-btn">SUBRIBE</div>

<footer class="abs footer"></footer>
<div class="abs f-head" style="left:98px">Quick Links</div>
<div class="abs f-rule" style="left:98px;width:88px"></div>
<ul class="abs links"><li>Home</li><li>About Us</li><li>Our Services</li><li>Our Network</li><li>News</li><li>Contact Us</li></ul>

<div class="abs f-head" style="left:219px">Latest News</div>
<svg class="abs" style="left:343px;top:1029px" width="18" height="9" viewBox="0 0 18 9"><path d="M5 1L1 4.5 5 8M13 1l4 3.5L13 8" fill="none" stroke="#fff" stroke-width="1.3"/></svg>
<div class="abs f-rule" style="left:219px;width:143px"></div>
<div class="abs news" style="top:1052px"><b>01-April-2014</b>Lorem ipsum dolor sit amet, consectetuer elit sed</div>
<div class="abs f-rule" style="left:219px;width:143px;top:1090px"></div>
<div class="abs news" style="top:1100px"><b>02-April-2014</b>Lorem ipsum dolor sit amet, consectetuer elit sed</div>

<div class="abs f-head" style="left:400px">Contact Detail</div>
<div class="abs f-rule" style="left:400px;width:140px"></div>
<div class="abs contact">
  <div class="c-row"><svg width="10" height="14" viewBox="0 0 10 14"><path d="M5 0a5 5 0 015 5c0 4-5 9-5 9S0 9 0 5a5 5 0 015-5z" fill="#a1cd39"/><circle cx="5" cy="5" r="1.8" fill="#1f1f1f"/></svg><div>12/F Harbourline Depot<br>40 Quayside Road<br>Port Verran<br>Eastbay</div></div>
  <div class="c-row big"><svg width="10" height="10" viewBox="0 0 10 10"><path d="M1 1l3 0 1 3-1.5 1c.6 1.3 1.2 1.9 2.5 2.5L7 6l3 1v3C5 10 0 5 1 1z" fill="#a1cd39"/></svg>555 0142 7700</div>
  <div class="c-row big"><svg width="10" height="10" viewBox="0 0 10 10"><path d="M1 1l3 0 1 3-1.5 1c.6 1.3 1.2 1.9 2.5 2.5L7 6l3 1v3C5 10 0 5 1 1z" fill="#a1cd39"/></svg>555 0142 7788</div>
  <div class="c-row"><svg width="10" height="8" viewBox="0 0 10 8"><rect width="10" height="8" fill="#a1cd39"/><path d="M0 0l5 4 5-4" fill="none" stroke="#1f1f1f"/></svg>info@vantorafreight.com</div>
</div>

<div class="abs f-head" style="left:579px">Location Map</div>
<div class="abs f-rule" style="left:579px;width:166px"></div>
<div class="abs map" role="img" aria-label="Street map showing the office location"></div>

<div class="abs bottom"></div>
<div class="abs copy">© 2015 VantoraFreightGroup. All Right Reserved</div>
<div class="abs social"><span>Plumetta</span><span>Chirrup</span><span>Worvanet</span><span>Vidora</span></div>

</body>
</html>
```